Business Card Design

This is a card for a dental orthodontics(braces) clinic.we provide patients life changing experience by changing their smiles. Our clinic features state of the art technology . Our preferred color scheme is blue,green and purple.
Our target market is teens and adults

I have attached a logo, it can be modified in my chosen colors
Updates

Lpleaas keep in mind dr. Fennimore is almost a fresh graduate and young, so the card should b fresh and vibrant

Reason: I have not received anything very satisfactory yet

• Dear all  the logo doesn't have to b something teeth related , it can b something based on simple lines like saome boxes etc

Industry/Entity Type

Dental

Contact Information for Business Card

BROCKWELL.FENNIMORE.
ORTHODONTICS

Olwen Fennimore, DDS, MS, MSD
Smile maker

Locations:
4815 W.Partridge Lane #312, Carrollton, TX 75009

6187 Meadow Brook Drive #408, Plano, TX 75098

812 Brindlemoor, Seagoville, TX 75159

Phone:972-555-0148

```html
<!DOCTYPE html>
<html lang="en">
<head>
<meta charset="utf-8">
<title>Brockwell Fennimore Orthodontics – Business Card</title>
<link rel="stylesheet" href="https://fonts.googleapis.com/css2?family=Lato:wght@400;700&display=swap">
<style>
  :root {
    --backdrop: #1c1c1e;
    --blue-deep: #0a4aa3;
    --blue-mid: #1672cc;
    --blue-glow: #3fc3f2;
    --band-blue: #1b7fc3;
    --white: #ffffff;
    --name-purple: #6a3f9f;
    --cred-blue: #2a74b8;
    --maker-green: #1d6a30;
  }
  * { box-sizing: border-box; margin: 0; padding: 0; }
  html, body {
    width: 1200px; height: 926px; overflow: hidden;
    background: var(--backdrop);
    font-family: "Lato", Arial, sans-serif;
  }
  .sheet {
    width: 1200px; height: 926px;
    display: flex; align-items: center; justify-content: center; gap: 40px;
  }
  .card {
    width: 540px; height: 309px; position: relative; overflow: hidden;
    flex: 0 0 auto;
  }
  /* Front */
  .card--front {
    background: radial-gradient(ellipse at 50% 36%, var(--blue-glow) 0%, var(--blue-mid) 45%, var(--blue-deep) 100%);
  }
  .wordmark__mark {
    position: absolute; left: 50%; top: 62px;
    width: 96px; height: 96px; margin-left: -48px;
    border-radius: 50%; background: var(--white);
  }
  .wordmark__name {
    position: absolute; left: 0; right: 0; top: 196px;
    text-align: center; white-space: nowrap;
    color: var(--white); font-weight: 400; font-size: 17px; letter-spacing: 2.6px;
  }
  /* Back */
  .card--back { background: var(--white); }
  .identity {
    position: absolute; left: 110px; top: 50px; white-space: nowrap;
  }
  .identity__name {
    color: var(--name-purple); font-size: 29px; font-weight: 400;
  }
  .identity__creds {
    color: var(--cred-blue); font-size: 14px; margin-left: 4px;
  }
  .identity__role {
    color: var(--maker-green); font-size: 21px; font-weight: 700;
    margin: 8px 0 0 38px; letter-spacing: 0.5px;
  }
  .contact-band {
    position: absolute; left: 0; right: 0; bottom: 0; height: 124px;
    background: var(--band-blue); color: var(--white);
    padding: 16px 18px 0 20px;
    display: flex; justify-content: space-between;
  }
  .locations { font-size: 13px; line-height: 1.45; font-style: normal; white-space: nowrap; }
  .lines { align-self: center; font-size: 15px; line-height: 1.45; margin-top: 14px; white-space: nowrap; }
  .lines b { font-weight: 700; }
</style>
</head>
<body>
<main class="sheet">
  <section class="card card--front" aria-label="Card front">
    <span class="wordmark__mark"></span>
    <p class="wordmark__name">BROCKWELL . FENNIMORE . ORTHODONTICS</p>
  </section>

  <section class="card card--back" aria-label="Card back">
    <div class="identity">
      <h1 class="identity__name">Olwen Fennimore <span class="identity__creds">DDS, MS, MSD</span></h1>
      <p class="identity__role">SMILE MAKER</p>
    </div>
    <div class="contact-band">
      <address class="locations">
        4815 W.Partridge Lane #312, Carrollton,<br>
        TX 75009 6187 Meadow Brook Drive #408,<br>
        Plano, TX 75098 812 Brindlemoor,<br>
        Seagoville, TX 75159
      </address>
      <div class="lines">
        <div><b>Phone</b>: 972-555-0148</div>
        <div><b>Fax</b> :972-555-0148</div>
      </div>
    </div>
  </section>
</main>
</body>
</html>
```